Business Cards

Need a neat design for a new business card

Industry/Entity Type

Residential Construction

Contact Information for Business Card

Company Name- KOVE Construction Inc.
Owner- Marcus Tolliver
Phone number- (555)203-7481
Email- kovecohomes@brindlemail.example
Facebook- www.socialpage.example/kovecohomes

Colors
fefdec

```html
<!DOCTYPE html>
<html lang="en">
<head>
<meta charset="utf-8">
<title>KOVE Construction Inc. — Business Card</title>
<link href="https://fonts.googleapis.com/css2?family=Cormorant+Garamond:wght@500&family=Roboto:wght@400;500;700&display=swap" rel="stylesheet">
<style>
  :root {
    --backdrop: #9a9a9a;
    --card: #171717;
    --ink: #fefdec;
  }
  html, body {
    margin: 0;
    padding: 0;
    width: 1021px;
    height: 1200px;
    overflow: hidden;
    background: var(--backdrop);
  }
  .card {
    position: absolute;
    left: 133px;
    width: 753px;
    height: 429px;
    background: var(--card);
    color: var(--ink);
    font-family: "Roboto", Arial, sans-serif;
  }
  .card--front { top: 119px; }
  .card--back { top: 651px; }

  .brand {
    position: absolute;
    left: 0;
    right: 0;
    display: flex;
    align-items: center;
    justify-content: center;
    gap: 14px;
    font-family: "Cormorant Garamond", Georgia, serif;
    font-weight: 500;
    color: var(--ink);
    letter-spacing: 0.06em;
    white-space: nowrap;
  }
  .brand__mark {
    width: 14px;
    height: 14px;
    background: var(--ink);
  }
  .card--front .brand { top: 180px; font-size: 48px; }
  .card--back .brand { top: 130px; font-size: 40px; }

  .contact {
    position: absolute;
    top: 294px;
    left: 0;
    right: 0;
  }
  .person {
    position: absolute;
    right: calc(753px - 355px);
    top: 6px;
    text-align: right;
    white-space: nowrap;
  }
  .person__name {
    font-weight: 700;
    font-size: 28px;
    line-height: 32px;
  }
  .person__role {
    font-size: 17px;
    line-height: 22px;
    margin-top: 4px;
  }
  .divider {
    position: absolute;
    left: 374px;
    top: 0;
    width: 1px;
    height: 61px;
    background: var(--ink);
  }
  .details {
    position: absolute;
    left: 395px;
    top: -5px;
    margin: 0;
    padding: 0;
    list-style: none;
    font-size: 17px;
    line-height: 25.5px;
    white-space: nowrap;
  }
  .details li {
    display: flex;
    align-items: center;
    gap: 8px;
  }
  .details svg {
    width: 13px;
    height: 13px;
    flex: none;
  }
</style>
</head>
<body>
  <section class="card card--front" aria-label="Card front">
    <div class="brand"><span class="brand__mark"></span>KOVE Construction Inc.</div>
  </section>

  <section class="card card--back" aria-label="Card back">
    <div class="brand"><span class="brand__mark"></span>KOVE Construction Inc.</div>

    <div class="contact">
      <div class="person">
        <div class="person__name">Marcus Tolliver</div>
        <div class="person__role">Owner</div>
      </div>
      <div class="divider"></div>
      <ul class="details">
        <li>
          <svg viewBox="0 0 24 24" aria-hidden="true"><path fill="var(--ink)" d="M6.6 10.8a15.5 15.5 0 0 0 6.6 6.6l2.2-2.2c.3-.3.7-.4 1-.2 1.1.4 2.3.6 3.6.6.6 0 1 .4 1 1V20c0 .6-.4 1-1 1A17 17 0 0 1 3 4c0-.6.4-1 1-1h3.5c.6 0 1 .4 1 1 0 1.3.2 2.5.6 3.6.1.3 0 .7-.2 1z"/></svg>
          (555)203-7481
        </li>
        <li>
          <svg viewBox="0 0 24 24" aria-hidden="true"><rect x="2" y="5" width="20" height="14" fill="var(--ink)"/><path d="M2 5l10 8 10-8" fill="none" stroke="var(--card)" stroke-width="1.6"/></svg>
          kovecohomes@brindlemail.example
        </li>
        <li>
          <svg viewBox="0 0 24 24" aria-hidden="true"><circle cx="12" cy="12" r="11" fill="var(--ink)"/></svg>
          www.socialpage.example/kovecohomes
        </li>
      </ul>
    </div>
  </section>
</body>
</html>
```